NEW YORK Plumbing/utility company 10 year anniversary business card

Looking For simple back and front business card would like to include a few things in description
We offer 24/7 emergency service
residential
commercial
industrial
municipal
services offered
Plumbing
hydro excavation
hydro jetting
Well pumps
Sewer pumps
water mains
sewer mains

```html
<!DOCTYPE html>
<html lang="en">
<head>
<meta charset="utf-8">
<title>Kestrel Creek Water &amp; Sewer – Business Card</title>
<link href="https://fonts.googleapis.com/css2?family=Source+Sans+3:wght@400;600;700&display=swap" rel="stylesheet">
<style>
  :root {
    --stage: #bfbfbf;
    --paper: #f4f4f4;
    --brand: #1a64a6;
    --brand-light: #1e9ad6;
    --wave-top: #43aee0;
    --wave-mid: #0b6cbc;
    --navy: #062c8a;
    --navy-dark: #000a45;
    --ink-light: #ffffff;
  }
  html, body {
    margin: 0;
    width: 1200px;
    height: 1200px;
    overflow: hidden;
    background: var(--stage);
    font-family: "Source Sans 3", sans-serif;
  }
  .card {
    position: absolute;
    width: 703px;
    height: 402px;
    background: var(--paper);
    overflow: hidden;
  }
  .card svg { display: block; width: 100%; height: 100%; }
  .card--front { left: 260px; top: 154px; }
  .card--back { left: 264px; top: 701px; }
  .brand-name { fill: var(--brand); font-weight: 700; }
  .brand-line { fill: var(--brand); font-weight: 400; }
  .brand-sub { fill: var(--brand-light); font-weight: 400; }
  .light-text { fill: var(--ink-light); font-weight: 600; font-size: 24px; }
  .heading-text { fill: var(--ink-light); font-weight: 700; font-size: 24px; }
  .note-text { fill: var(--brand); font-weight: 600; font-size: 20px; }
  .rule { stroke: #8ea6d8; stroke-width: 1; }
  .icon { fill: var(--ink-light); }
</style>
</head>
<body>

<svg width="0" height="0" style="position:absolute">
  <defs>
    <linearGradient id="gradBand" x1="0" y1="0" x2="0" y2="1">
      <stop offset="0" stop-color="var(--wave-top)"/>
      <stop offset="0.25" stop-color="var(--wave-mid)"/>
      <stop offset="0.5" stop-color="var(--navy)"/>
      <stop offset="1" stop-color="var(--navy-dark)"/>
    </linearGradient>
  </defs>
</svg>

<div class="card card--front">
  <svg viewBox="0 0 950 543" aria-label="Front of business card">
    <rect class="wave-band" x="0" y="340" width="950" height="203" fill="url(#gradBand)" role="img" aria-label="Layered blue water waves"/>
    <g class="brand-block">
      <circle cx="398" cy="232" r="20" fill="var(--brand)"/>
      <text class="brand-name" x="428" y="254" font-size="66">KCW</text>
      <text class="brand-line" x="490" y="292" font-size="22" text-anchor="middle" letter-spacing="3">KESTREL CREEK</text>
      <text class="brand-sub" x="490" y="316" font-size="15" text-anchor="middle" letter-spacing="3">WATER &amp; SEWER</text>
    </g>
    <g class="contact">
      <path class="icon" d="M112,466 a8,8 0 0 1 8,8 c0,6 -8,15 -8,15 c0,0 -8,-9 -8,-15 a8,8 0 0 1 8,-8z M112,470 a4,4 0 1 0 0.01,0z" fill-rule="evenodd"/>
      <text class="light-text" x="146" y="482">Address</text>
      <path class="icon" d="M105,505 l5,-2 l4,7 l-3,3 c1,3 4,6 7,7 l3,-3 l7,4 l-2,5 c-10,1 -22,-11 -21,-21z"/>
      <text class="light-text" x="146" y="521">+1 555 010 2480</text>
      <path class="icon" d="M604,469 h21 v14 h-21z"/>
      <path d="M604,469 l10.5,8 l10.5,-8 M604,483 l8,-7 M625,483 l-8,-7" stroke="var(--navy)" stroke-width="1.6" fill="none"/>
      <text class="light-text" x="647" y="482">hello@kcwater.example</text>
      <path class="icon" d="M609,498 l0,20 l5,-5 l4,8 l3,-1.5 l-4,-8 l7,0z"/>
      <text class="light-text" x="656" y="512">www.kcwater.example</text>
    </g>
  </svg>
</div>

<div class="card card--back">
  <svg viewBox="0 0 950 543" aria-label="Back of business card">
    <rect class="wave-band" x="0" y="185" width="950" height="358" fill="url(#gradBand)" role="img" aria-label="Layered blue water waves"/>
    <g class="brand-block">
      <circle cx="86" cy="22" r="14" fill="var(--brand)"/>
      <text class="brand-name" x="108" y="38" font-size="44">KCW</text>
      <text class="brand-line" x="735" y="18" font-size="22" text-anchor="middle" letter-spacing="3">KESTREL CREEK</text>
      <text class="brand-sub" x="735" y="42" font-size="15" text-anchor="middle" letter-spacing="3">WATER &amp; SEWER</text>
    </g>
    <g class="highlights">
      <text class="note-text" x="71" y="120">Celebrating 10 Years</text>
      <text class="note-text" x="879" y="120" text-anchor="end">24/7 Emergency Service</text>
    </g>
    <g class="services">
      <text class="heading-text" x="71" y="340">Services Offered:</text>
      <line class="rule" x1="71" y1="350" x2="484" y2="350"/>
      <text class="light-text" x="71" y="398">Plumbing</text>
      <text class="light-text" x="71" y="427">Hydro excavation</text>
      <text class="light-text" x="71" y="456">Hydro jetting</text>
      <text class="light-text" x="71" y="484">Well pumps</text>
      <text class="light-text" x="342" y="398">Sewer pumps</text>
      <text class="light-text" x="342" y="427">Water mains</text>
      <text class="light-text" x="342" y="456">Sewer mains</text>
    </g>
    <g class="capacity">
      <text class="heading-text" x="772" y="340">Capacity:</text>
      <line class="rule" x1="772" y1="350" x2="902" y2="350"/>
      <text class="light-text" x="772" y="398">Residential</text>
      <text class="light-text" x="772" y="427">Commercial</text>
      <text class="light-text" x="772" y="456">Industrial</text>
      <text class="light-text" x="772" y="484">Municipal</text>
    </g>
  </svg>
</div>

</body>
</html>
```